Brochure design for moving and cleaning company

Hello

We need a NEW design of our brochure that we already have. Please check the brochure and give us a creative, professional and new design of it.

Here the brochure:

https://www.filecrate.example/s/zq7hn2b0t81kxc4/0-1Rundum%20Trazo%20Mail4.9.17%20Trazo%202014%20Kopie%202.indd?dl=0

https://www.filecrate.example/s/pwrtkaledx5vnoo/2016%20Druck%201%20Rundum%202016%20Brosch%C3%BCre%20Druck.pdf?dl=0

I added the new text for the brochure and new logos and pictures.

Kind regards

T. Benschell

Industry/Entity Type

Moving Company

Colors
ec1f27

Requirements
Must have
• http://quillvanta.example/red-brochure-template/red-brochure-template-red-and-white-corporate-brochure-template-vector-free-download-free/
Nice to have

```html
<!DOCTYPE html>
<html lang="de">
<head>
<meta charset="utf-8">
<title>Umzugswerk Broschüre</title>
<link rel="stylesheet" href="https://fonts.googleapis.com/css2?family=Montserrat:wght@500;600;700;800&family=Open+Sans:wght@400;600&display=swap">
<style>
:root{
  --red:#ec1f27;
  --red-dark:#b8141b;
  --ink:#1d1d1f;
  --panel:#232325;
  --paper:#f4f4f4;
  --grey:#cfcfcf;
  --text:#444;
  --stage:#b9b9b9;
}
*{margin:0;padding:0;box-sizing:border-box}
html,body{width:938px;height:1200px;overflow:hidden}
body{background:var(--stage);font-family:"Open Sans",sans-serif;color:var(--text);position:relative}
.page-label{position:absolute;width:366px;text-align:center;font:400 19px "Open Sans",sans-serif;color:#222}
.page{position:absolute;width:366px;height:516px;background:linear-gradient(180deg,#fafafa,#ececec);overflow:hidden;box-shadow:0 3px 10px rgba(0,0,0,.25)}
.page::before{content:"";position:absolute;left:0;top:0;right:0;height:4px;background:var(--red);z-index:3}
.p1{left:92px;top:60px}.p2{left:472px;top:60px}.p3{left:92px;top:620px}.p4{left:472px;top:620px}
.abs{position:absolute}
.brand{position:absolute;display:flex;align-items:center;gap:7px;font:800 27px "Montserrat",sans-serif;letter-spacing:1px;color:var(--ink);white-space:nowrap}
.brand .mark{width:26px;height:26px;background:var(--red)}
.brand.small{font-size:13px;gap:4px;color:#555}
.brand.small .mark{width:13px;height:13px}
.url{position:absolute;font:600 6.4px "Montserrat",sans-serif;letter-spacing:1.6px;color:var(--ink)}
.footer-deco{position:absolute;left:0;bottom:0;width:366px;height:80px}
/* page 1 */
.hero{left:0;top:78px;width:366px;height:258px}
.photo{position:absolute;left:0;top:104px;width:212px;height:208px;background:linear-gradient(135deg,#cdb89a,#e9e2d7 55%,#8b97ad)}
.welcome{left:8px;top:350px;width:350px;text-align:center;font:700 13.5px/1.25 "Montserrat",sans-serif;color:var(--ink)}
.welcome span{display:block;white-space:nowrap}
.welcome .accent{color:var(--red);font-size:15px}
.intro{left:24px;top:394px;width:320px;text-align:center;font-size:6.1px;line-height:1.45}
.intro p+p{margin-top:6px}
.rule-dot{position:absolute;height:1px;background:var(--red)}
.rule-dot::before,.rule-dot::after{content:"";position:absolute;top:-2px;width:5px;height:5px;border:1px solid var(--red);border-radius:50%;background:#fff}
.rule-dot::before{left:-3px}.rule-dot::after{right:-3px}
/* page 2 */
.history{left:49px;top:98px;width:265px;height:325px;background:var(--panel);padding:36px 22px 0 37px;color:#cfcfcf;font-size:6.1px;line-height:1.6}
.history h2{font:700 15px "Montserrat",sans-serif;color:var(--red);text-align:center;margin-bottom:12px;margin-left:-14px}
.history p{text-align:justify;margin-bottom:8px}
/* page 3/4 headers */
.section-title{left:24px;top:22px;font:700 16px/1.25 "Montserrat",sans-serif;color:var(--red)}
.subline{left:24px;top:64px;font-size:8px;color:var(--ink)}
.services{left:25px;top:90px;width:325px;display:grid;grid-template-columns:131px 183px;grid-auto-rows:117px;gap:4px 10px}
.service{border:1px solid #d4d4d4;background:rgba(255,255,255,.55);text-align:center;padding:10px 8px 0}
.service svg{width:28px;height:26px;display:block;margin:0 auto 6px}
.service h3{font:700 6.6px/1.3 "Montserrat",sans-serif;color:var(--red);margin-bottom:4px}
.service p{font-size:5.4px;line-height:1.45;color:#555}
.service.dense p{font-size:4.8px}
/* price list */
.prices{left:43px;top:90px;width:275px;height:162px;border:1px solid #d6d6d6;background:rgba(255,255,255,.4)}
.prices .head{height:20px;background:var(--red);color:#fff;font:700 6.5px "Montserrat",sans-serif;display:flex;align-items:center;justify-content:space-around}
.prices table{width:100%;border-collapse:collapse;margin-top:9px;font:500 7.6px "Montserrat",sans-serif}
.prices td{height:19.6px;padding-left:8px;color:var(--ink)}
.prices td.tr{color:var(--red);font-weight:600;padding-left:0}
.prices td.ic{width:26px}
.prices td.ic svg{width:13px;height:8px;display:block}
.extras{left:43px;width:275px;font:500 7px/1.3 "Montserrat",sans-serif;color:var(--ink)}
.extras b{color:var(--red);font-weight:700}
.truck-photo{left:72px;top:372px;width:208px;height:90px;border-radius:6px;background:linear-gradient(180deg,#e7e7e7 0%,#e7e7e7 25%,#d4262b 26%,#a81a1e 80%,#333 100%)}
</style>
</head>
<body>

<div class="page-label" style="left:92px;top:18px">Page 1</div>
<div class="page-label" style="left:472px;top:18px">Page 2</div>
<div class="page-label" style="left:92px;top:1152px">Page 3</div>
<div class="page-label" style="left:472px;top:1152px">Page 4</div>

<!-- PAGE 1 -->
<section class="page p1">
  <div class="brand" style="left:36px;top:28px">UMZUGSWERK<span class="mark"></span></div>
  <svg class="abs hero" viewBox="0 0 366 258">
    <polygon points="180,2 290,2 310,38 366,90 366,250 290,250 340,150" fill="var(--ink)"/>
    <polygon points="170,2 294,2 330,48 300,90 260,250 198,250 272,130" fill="var(--red)"/>
    <polygon points="188,2 220,2 302,130 232,250 216,250 282,130" fill="var(--red-dark)"/>
    <polygon points="250,250 282,200 300,200 268,250" fill="#fff"/>
    <line x1="0" y1="2" x2="294" y2="2" stroke="var(--red)" stroke-width="1"/>
    <line x1="294" y1="2" x2="325" y2="50" stroke="var(--red)" stroke-width="1"/>
    <circle cx="325" cy="50" r="2.5" fill="#fff" stroke="var(--red)"/>
    <rect x="0" y="212" width="270" height="40" fill="var(--red)"/>
    <rect x="0" y="234" width="220" height="2" fill="#fff" opacity=".4"/>
    <rect x="0" y="241" width="200" height="2" fill="#fff" opacity=".3"/>
  </svg>
  <div class="photo" role="img" aria-label="Foto: lächelndes Paar sitzt zwischen Umzugskartons in der neuen Wohnung"></div>
  <div class="rule-dot" style="left:24px;top:337px;width:320px"></div>
  <h1 class="abs welcome"><span>HERZLICH WILLKOMMEN BEI UMZUGSWERK,</span><span class="accent">REGAL TRANSIT &amp; GLANZWERK</span></h1>
  <div class="abs intro">
    <p>Stressfrei, sorglos und entspannt ins neue Wohnglück! Für viele Kunden, denen ein Umzug bevorsteht, leider ein Fremdwort. Auf der Suche nach zuverlässigen und professionellen Firmen, findet man des Öfteren Anbieter oder Plattformen, die mehrere Offerten innert kurzer Zeit senden und mit günstigen Angeboten locken. Der Kunde istoft nach der Ausführung enttäuscht.</p>
    <p>Unser stetiges Ziel ist es, ein gutes Preis-Leistungsverhältnis anzubieten, welche dem Kunden und dem Geschäft zu Gunsten kommt, um die komplette Dienstleistung vom Umzug bis zur Endreinigung zur vollsten Zufriedenheit zu erbringen.</p>
  </div>
  <div class="url" style="left:127px;top:491px">www.umzugswerk.example</div>
  <div class="abs" style="left:0;bottom:0;width:366px;height:4px;background:var(--red)"></div>
</section>

<!-- PAGE 2 -->
<section class="page p2">
  <div class="brand" style="left:64px;top:40px">UMZUGSWERK<span class="mark"></span></div>
  <div class="abs history">
    <h2>FIRMENGESCHICHTE</h2>
    <p>Vor knapp 10 Jahren wurde die Reinigungsfirma Glanzwerk gegründet. Wir haben in dieser Zeit sehr viel Erfahrung im Bereich Umzugsreinigungen, Wohnungsreinigungen und Fensterreinigungen gesammelt und haben seit dem Jahr 2015 mit Umzüge, Räumungen und Entsorgungen unser Dienstleistungsbereich in der Deutschschweiz erweitert und die Firma Umzugswerk gegründet.</p>
    <p>Um die Firma Umzugswerk im Bereich Umzüge, Räumungen und Entsorgungen weiter zu expandieren, haben wir uns seit November 2017 mit der Firma Regal Transit in der Region Zürich und Winterthur zusammengeschlossen.</p>
    <p>Dadurch konnten wir neue Fahrzeuge und Inventar erwerben um professionellere &amp; komplexere Aufträge &amp; Dienstleistungen zu erbringen.</p>
    <p>Mit bereits über 2000 ausgeführten Endreinigungen und Umzügen in der Deutschschweiz, sind wir ihr starker Partner, wenn es um das Thema Umzüge und Endreinigungen geht.</p>
    <p>Wir bedanken uns bei unserer Kundschaft, sowie bei unseren zukünftigen Auftraggebern für ihr Vertrauen.</p>
  </div>
  <svg class="abs" style="left:0;top:0" width="366" height="440" viewBox="0 0 366 440">
    <polyline points="0,121 297,121 297,161" fill="none" stroke="var(--red)" stroke-width=".8"/>
    <circle cx="297" cy="161" r="2" fill="var(--panel)" stroke="#fff" stroke-width=".8"/>
    <polyline points="64,362 64,402 366,402" fill="none" stroke="var(--red)" stroke-width=".8"/>
    <circle cx="64" cy="362" r="2" fill="var(--panel)" stroke="#fff" stroke-width=".8"/>
  </svg>
  <svg class="footer-deco" viewBox="0 0 366 80">
    <polygon points="40,30 366,30 366,50 60,50" fill="#d2d2d2"/>
    <polygon points="0,0 0,80 366,80 366,60 230,60 210,45 50,45" fill="var(--red)"/>
    <polygon points="230,60 366,60 366,80 250,80" fill="var(--ink)"/>
  </svg>
  <div class="url" style="left:23px;top:498px;color:#fff">www.umzugswerk.example</div>
</section>

<!-- PAGE 3 -->
<section class="page p3">
  <h2 class="abs section-title">UNSERE<br>DIENSTLEISTUNGEN</h2>
  <div class="brand small" style="left:229px;top:22px">UMZUGSWERK<span class="mark"></span></div>
  <div class="abs subline">Kostenlose Beratung und Besichtigung vor Ort!</div>
  <svg class="abs" style="left:0;top:72px" width="300" height="8"><line x1="0" y1="4" x2="232" y2="4" stroke="var(--red)" stroke-width=".8"/><circle cx="234" cy="4" r="2" fill="#fff" stroke="var(--red)"/></svg>
  <div class="abs services">
    <div class="service">
      <svg viewBox="0 0 28 26"><path d="M4 9h20v15H4z" fill="var(--ink)"/><path d="M4 9l4-6h12l4 6" fill="none" stroke="var(--ink)" stroke-width="2"/><path d="M14 11v9M11 14l3-3 3 3" stroke="#fff" stroke-width="1.5" fill="none"/></svg>
      <h3>PRIVAT- ODER<br>FIRMENUMZUG</h3>
      <p>Wir übernehmen den stressigen Umzug für Sie, auf Wunsch inkl. Montage- und Demontage der Möbel. Versicherung inklusive!</p>
    </div>
    <div class="service">
      <svg viewBox="0 0 28 26"><circle cx="14" cy="13" r="11" fill="var(--ink)"/><path d="M9 13l3.5 3.5L19 10" stroke="#fff" stroke-width="2" fill="none"/></svg>
      <h3>UMZUGSREINIGUNG INKL.<br>100% ABNAHMEGARANTIE</h3>
      <p>Professionelle Reinigung dank unserer Reinigungsfirma! Gib die alte Wohnung den Profis in die Hand und lass sie nach dem Umzug von uns endreinigen – inkl. Abnahmegarantie!</p>
    </div>
    <div class="service">
      <svg viewBox="0 0 28 26"><circle cx="14" cy="13" r="11" fill="none" stroke="var(--ink)" stroke-width="2"/><rect x="9" y="8" width="10" height="10" fill="var(--ink)"/></svg>
      <h3>LAGERUNG</h3>
      <p>Ob Umzug, Umbau oder Auslandsaufenthalt – wir lagern für Sie Möbel, Akten und weiteres Inventar sicher und zuverlässig.</p>
    </div>
    <div class="service">
      <svg viewBox="0 0 28 26"><rect x="3" y="7" width="15" height="11" fill="var(--ink)"/><path d="M18 10h5l3 4v4h-8z" fill="var(--ink)"/><circle cx="8" cy="20" r="2.5" fill="var(--ink)"/><circle cx="21" cy="20" r="2.5" fill="var(--ink)"/></svg>
      <h3>TRANSPORT</h3>
      <p>Lassen Sie Ihre Wertsachen oder Güter durch unsere Spedition sicher von A nach B transportieren. Zuverlässig, schnell und inkl. Versicherung. Bei uns auch 24 Std. Expressdienst!</p>
    </div>
    <div class="service dense">
      <svg viewBox="0 0 28 26"><path d="M6 3h3l3 17h10" fill="none" stroke="var(--ink)" stroke-width="2"/><rect x="13" y="8" width="9" height="10" fill="var(--ink)"/><circle cx="12" cy="22" r="2" fill="var(--ink)"/></svg>
      <h3>RÄUMUNG</h3>
      <p>Wir räumen Ihr Wohnobjekt vom Keller bis zum Estrich und gehen dabei auf Ihre individuellen Wünsche ein. Von der Demontage der Möbel über den Abtransport bis hin zur umweltgerechten Entsorgung erledigen wir alles aus einer Hand. So übergeben Sie Ihre Räume sauber und ohne Aufwand an Vermieter oder Nachmieter.</p>
    </div>
    <div class="service dense">
      <svg viewBox="0 0 28 26"><path d="M14 3l5 8h-10zM5 22l4-8 5 8zM23 22h-9l4-8z" fill="var(--ink)"/></svg>
      <h3>ENTRÜMPELUNG</h3>
      <p>Egal ob alte Möbel, Waschmaschinen, Einbauschränke, Betten usw. – wenn Gegenstände nicht mehr gebraucht werden, müssen Sie nach den Richtlinien der Abfalltrennung entsorgt werden. Sperrgut oder nicht verwertbare Abfälle – wir kennen uns damit bestens aus und unterstützen Sie gerne mit unserem Entsorgungs-Service.</p>
    </div>
  </div>
  <svg class="footer-deco" viewBox="0 0 366 80">
    <polygon points="40,30 366,30 366,50 60,50" fill="#d2d2d2"/>
    <polygon points="0,0 0,80 366,80 366,60 230,60 210,45 50,45" fill="var(--red)"/>
    <polygon points="230,60 366,60 366,80 250,80" fill="var(--ink)"/>
  </svg>
  <div class="url" style="left:23px;top:498px;color:#fff">www.umzugswerk.example</div>
</section>

<!-- PAGE 4 -->
<section class="page p4">
  <h2 class="abs section-title" style="top:24px">PREISLISTE UMZUG</h2>
  <div class="brand small" style="left:229px;top:22px">UMZUGSWERK<span class="mark"></span></div>
  <svg class="abs" style="left:0;top:47px" width="300" height="8"><line x1="0" y1="4" x2="192" y2="4" stroke="var(--red)" stroke-width=".8"/><circle cx="194" cy="4" r="2" fill="#fff" stroke="var(--red)"/></svg>
  <div class="abs prices">
    <div class="head"><span>PREISLISTE 2018</span><span>BUCHUNG MIND. 4 STD</span></div>
    <table>
      <tr><td class="ic"><svg viewBox="0 0 13 8"><rect x="0" y="1" width="8" height="5" fill="#555"/><path d="M8 3h3l2 2v1H8z" fill="#555"/><circle cx="3" cy="7" r="1" fill="#555"/><circle cx="10" cy="7" r="1" fill="#555"/></svg></td><td class="tr">1 TRUCK 2PEOPLE</td><td>20m3 und 2 Männer</td><td>160.-/Std.</td></tr>
      <tr><td class="ic"><svg viewBox="0 0 13 8"><rect x="0" y="1" width="8" height="5" fill="#555"/><path d="M8 3h3l2 2v1H8z" fill="#555"/><circle cx="3" cy="7" r="1" fill="#555"/><circle cx="10" cy="7" r="1" fill="#555"/></svg></td><td class="tr">1 TRUCK 3PEOPLE</td><td>20m3 und 3 Männer</td><td>225.-/Std.</td></tr>
      <tr><td class="ic"><svg viewBox="0 0 13 8"><rect x="0" y="1" width="8" height="5" fill="#555"/><path d="M8 3h3l2 2v1H8z" fill="#555"/><circle cx="3" cy="7" r="1" fill="#555"/><circle cx="10" cy="7" r="1" fill="#555"/></svg></td><td class="tr">2 TRUCK 4PEOPLE</td><td>40m3 und 4 Männer</td><td>300.-/Std.</td></tr>
      <tr><td class="ic"><svg viewBox="0 0 13 8"><rect x="0" y="1" width="8" height="5" fill="#555"/><path d="M8 3h3l2 2v1H8z" fill="#555"/><circle cx="3" cy="7" r="1" fill="#555"/><circle cx="10" cy="7" r="1" fill="#555"/></svg></td><td class="tr">2 TRUCK 5PEOPLE</td><td>40m3 und 5 Männer</td><td>360.-/Std.</td></tr>
      <tr><td class="ic"><svg viewBox="0 0 13 8"><rect x="0" y="1" width="8" height="5" fill="#555"/><path d="M8 3h3l2 2v1H8z" fill="#555"/><circle cx="3" cy="7" r="1" fill="#555"/><circle cx="10" cy="7" r="1" fill="#555"/></svg></td><td class="tr">3 TRUCK 5PEOPLE</td><td>60m3 und 5 Männer</td><td>375.-/Std.</td></tr>
      <tr><td class="ic"><svg viewBox="0 0 13 8"><rect x="0" y="1" width="8" height="5" fill="#555"/><path d="M8 3h3l2 2v1H8z" fill="#555"/><circle cx="3" cy="7" r="1" fill="#555"/><circle cx="10" cy="7" r="1" fill="#555"/></svg></td><td class="tr">3 TRUCK 6PEOPLE</td><td>60m3 und 6 Männer</td><td>450.-/Std.</td></tr>
    </table>
  </div>
  <div class="abs extras" style="top:275px;display:flex;justify-content:space-between">
    <div><b>HIGH-TECH MÖBELLIFT</b><br>Inkl. Bedienmann</div><div>27 Meter ca. 9. Stock</div><div>135.-/ Std.</div>
  </div>
  <div class="abs extras" style="top:307px;display:flex;justify-content:space-between">
    <div><b>UMZUGSVERSICHERUNG BIS CHF 50000.<br>UMZUGSVERSICHERUNG BIS CHF 100000.</b></div><div>CHF 90.<br>CHF 130.</div>
  </div>
  <div class="abs extras" style="top:339px">Wir arbeiten nach den allgemeinen Bedingungen der Möbeltransporteure des schweizerischen Transportverbandes STVB</div>
  <div class="abs truck-photo" role="img" aria-label="Foto: roter Oldtimer-Lastwagen mit weissem Tankaufbau"></div>
  <svg class="footer-deco" viewBox="0 0 366 80">
    <polygon points="40,30 366,30 366,50 60,50" fill="#d2d2d2"/>
    <polygon points="0,0 0,80 366,80 366,60 230,60 210,45 50,45" fill="var(--red)"/>
    <polygon points="230,60 366,60 366,80 250,80" fill="var(--ink)"/>
  </svg>
  <div class="url" style="left:23px;top:498px;color:#fff">www.umzugswerk.example</div>
</section>

</body>
</html>
```